My business is Property developing Stationary

I want business card and stationery. Please have the formate so I can edit details on card and stationary.

Please see my logo and on the back of the card I want it same red as my logo and I will provide copy that I want on the back of the card.

Also need an email signature

On the business card and email signature add below copy:
Project Management- Acquisitions- Syndicates- Joint Ventures

Target Market(s)

Property investors

Industry/Entity Type

Business

Requirements
Must have
• Reflect my Logo

```html
<!DOCTYPE html>
<html lang="en">
<head>
<meta charset="utf-8">
<title>Varden Property Group — Letterhead</title>
<link rel="stylesheet" href="https://fonts.googleapis.com/css2?family=Questrial&display=swap">
<style>
  :root {
    --brand-red: #d9352a;
    --ink: #1d1d1d;
    --paper: #f4f4f4;
    --backdrop: #d2d1d1;
  }
  * { margin: 0; padding: 0; box-sizing: border-box; }
  html, body {
    width: 1200px;
    height: 900px;
    overflow: hidden;
    background: var(--backdrop);
    font-family: "Questrial", sans-serif;
  }
  .letterhead {
    position: absolute;
    left: 295px;
    top: 20px;
    width: 610px;
    height: 860px;
    background: var(--paper);
    overflow: hidden;
  }
  .brand {
    position: absolute;
    left: 44px;
    top: 66px;
    display: flex;
    align-items: center;
    gap: 8px;
  }
  .brand-square {
    width: 14px;
    height: 14px;
    background: var(--brand-red);
  }
  .brand-name {
    font-size: 24px;
    color: var(--brand-red);
    letter-spacing: 0.5px;
    line-height: 1;
  }
  .contact-line {
    position: absolute;
    left: 43px;
    top: 826px;
    display: flex;
    align-items: center;
    font-size: 8.5px;
    color: var(--ink);
    white-space: nowrap;
  }
  .contact-address { margin-right: 18px; }
  .contact-item {
    display: flex;
    align-items: center;
    gap: 4px;
    margin-right: 14px;
  }
  .contact-icon {
    width: 9px;
    height: 9px;
    display: block;
  }
  .footer-bar {
    position: absolute;
    left: 0;
    bottom: 0;
    width: 610px;
    height: 10px;
  }
  .corner-accent {
    position: absolute;
    right: 0;
    bottom: 0;
    width: 90px;
    height: 70px;
  }
</style>
</head>
<body>
  <main class="letterhead">
    <header class="brand">
      <span class="brand-square"></span>
      <span class="brand-name">Varden Property Group</span>
    </header>

    <footer class="contact-line">
      <span class="contact-address">Level 12, Harbour House, 18 Quay Lane, Sydney</span>
      <span class="contact-item">
        <svg class="contact-icon" viewBox="0 0 10 10" aria-hidden="true">
          <rect width="10" height="10" rx="1.5" fill="var(--brand-red)"/>
          <path d="M3 2.2 L4.2 3.6 L3.6 4.3 Q4.5 5.8 5.7 6.4 L6.4 5.8 L7.8 7 L7 8 Q3.5 7.4 2 3 Z" fill="#fff"/>
        </svg>
        1300 555 218
      </span>
      <span class="contact-item">
        <svg class="contact-icon" viewBox="0 0 10 10" aria-hidden="true">
          <rect width="10" height="10" rx="1.5" fill="var(--brand-red)"/>
          <rect x="2" y="3" width="6" height="4.2" fill="none" stroke="#fff" stroke-width="0.9"/>
          <path d="M2 3 L5 5.4 L8 3" fill="none" stroke="#fff" stroke-width="0.9"/>
        </svg>
        info@varden.com
      </span>
      <span class="contact-item">
        <svg class="contact-icon" viewBox="0 0 10 10" aria-hidden="true">
          <rect width="10" height="10" rx="1.5" fill="var(--brand-red)"/>
          <circle cx="5" cy="5" r="2.8" fill="none" stroke="#fff" stroke-width="0.8"/>
          <path d="M2.2 5 H7.8 M5 2.2 Q3.4 5 5 7.8 M5 2.2 Q6.6 5 5 7.8" fill="none" stroke="#fff" stroke-width="0.6"/>
        </svg>
        www.varden.com
      </span>
    </footer>

    <svg class="footer-bar" viewBox="0 0 610 10" preserveAspectRatio="none" aria-hidden="true">
      <polygon points="0,0 525,0 515,10 0,10" fill="var(--brand-red)"/>
    </svg>

    <svg class="corner-accent" viewBox="0 0 90 70" aria-hidden="true">
      <polygon points="90,8 90,70 10,70" fill="var(--ink)"/>
      <polygon points="90,38 90,70 50,70" fill="var(--brand-red)"/>
    </svg>
  </main>
</body>
</html>
```